New Business Card Design Project

Hi! I would like for you to design a business card for our aesthetic injections business. We offer Zelvia, filler, skin care. I would like it to be elegant, feminine, modern and sleek/clean. I like black/gold foil/ivory/parchment colors. It can be either one or two sided. I would like matte black with gold foil logo on one side and ivory with gold foil information on the other side

Target Market(s)

target market is the discerning woman who wants to look her best

Industry/Entity Type

beauty

Contact Information for Business Card

logo, name, phone, email, website, instagram, facebook, location

Requirements
Must have
• logo and info
Nice to have
• the icons for cell, instagram, email, fb etc
Should not have
• images of people

```html
<!DOCTYPE html>
<html lang="en">
<head>
<meta charset="utf-8">
<title>The Velour Studio – Business Card</title>
<link href="https://fonts.googleapis.com/css2?family=Montserrat:wght@300;400&family=Allura&display=swap" rel="stylesheet">
<style>
  :root {
    --backdrop: #2b2b2c;
    --card-black: #221e1f;
    --card-white: #fbfbfb;
    --ivory: #ddd3c2;
    --ink: #1c1a1b;
    --muted: #a9a6a4;
    --silver-light: #f2f2f2;
    --silver-dark: #8d8d8d;
  }
  html, body {
    margin: 0;
    width: 1200px;
    height: 900px;
    overflow: hidden;
    background: var(--backdrop);
    font-family: "Montserrat", Arial, sans-serif;
  }
  .stage {
    position: relative;
    width: 1200px;
    height: 900px;
  }
  .card {
    position: absolute;
    left: 285px;
    width: 630px;
    height: 360px;
    border-radius: 22px;
    overflow: hidden;
    background: var(--card-black);
    box-shadow: 0 10px 30px rgba(0,0,0,0.45);
  }
  .card--back { top: 50px; }
  .card--front { top: 490px; }

  /* Brand mark: name inside a plain circle */
  .brand {
    position: absolute;
    width: 190px;
    height: 190px;
    border-radius: 50%;
    display: flex;
    flex-direction: column;
    align-items: center;
    justify-content: center;
    text-align: center;
    font-weight: 300;
    text-transform: uppercase;
    letter-spacing: 0.28em;
    line-height: 1.9;
    font-size: 17px;
  }
  .brand--back {
    left: 220px;
    top: 85px;
    border: 2px solid var(--ivory);
    color: var(--ivory);
  }
  .brand--front {
    left: 395px;
    top: 36px;
    width: 175px;
    height: 175px;
    font-size: 15px;
    border: 1.5px solid var(--ink);
    color: var(--ink);
  }

  .front-panel {
    position: absolute;
    inset: 0;
  }

  .person {
    position: absolute;
    left: 44px;
    top: 60px;
    color: var(--ivory);
  }
  .person__role {
    font-size: 13px;
    font-weight: 300;
    letter-spacing: 0.04em;
  }
  .person__name {
    font-family: "Allura", cursive;
    font-size: 46px;
    line-height: 1;
    margin-top: 2px;
  }

  .contact {
    position: absolute;
    left: 44px;
    bottom: 34px;
    margin: 0;
    padding: 0;
    list-style: none;
    color: var(--muted);
    font-size: 13px;
    font-weight: 300;
  }
  .contact__item {
    display: flex;
    align-items: flex-start;
    gap: 10px;
    margin-top: 10px;
  }
  .contact__icon {
    width: 14px;
    height: 14px;
    flex: none;
    margin-top: 1px;
    fill: var(--muted);
  }

  .social {
    position: absolute;
    right: 44px;
    bottom: 100px;
    display: flex;
    align-items: center;
    gap: 8px;
    color: var(--ink);
    font-size: 12px;
    font-weight: 400;
    letter-spacing: 0.04em;
  }
  .social__mark {
    width: 14px;
    height: 14px;
    background: var(--ink);
    border-radius: 3px;
  }
</style>
</head>
<body>
<main class="stage">

  <section class="card card--back" aria-label="Card back">
    <div class="brand brand--back">
      <span>The</span>
      <span>Velour</span>
      <span>Studio</span>
    </div>
  </section>

  <section class="card card--front" aria-label="Card front">
    <svg class="front-panel" width="630" height="360" viewBox="0 0 630 360" aria-hidden="true">
      <defs>
        <linearGradient id="silverEdge" x1="0" y1="0" x2="1" y2="1">
          <stop offset="0" stop-color="#8d8d8d"/>
          <stop offset="0.5" stop-color="#f2f2f2"/>
          <stop offset="1" stop-color="#8d8d8d"/>
        </linearGradient>
      </defs>
      <path d="M 300 0 C 395 0, 355 360, 440 360 L 630 360 L 630 0 Z"
            fill="url(#silverEdge)"/>
      <path d="M 312 0 C 405 0, 368 354, 450 360 L 630 360 L 630 0 Z"
            fill="#fbfbfb"/>
    </svg>

    <div class="brand brand--front">
      <span>The</span>
      <span>Velour</span>
      <span>Studio</span>
    </div>

    <div class="person">
      <div class="person__role">Director</div>
      <div class="person__name">Mara Ellison</div>
    </div>

    <ul class="contact">
      <li class="contact__item">
        <svg class="contact__icon" viewBox="0 0 16 16" aria-hidden="true"><path d="M3 1h3l1.5 4-2 1.2a9 9 0 0 0 4.3 4.3L11 8.5l4 1.5v3a2 2 0 0 1-2 2C6.9 15 1 9.1 1 3a2 2 0 0 1 2-2z"/></svg>
        <span>(555) 014 2287</span>
      </li>
      <li class="contact__item">
        <svg class="contact__icon" viewBox="0 0 16 16" aria-hidden="true"><path d="M1 3h14v10H1z M1.5 3.5 8 9l6.5-5.5" fill="none" stroke="#a9a6a4" stroke-width="1.4"/></svg>
        <span>hello@velourstudio.com</span>
      </li>
      <li class="contact__item">
        <svg class="contact__icon" viewBox="0 0 16 16" aria-hidden="true"><g fill="none" stroke="#a9a6a4" stroke-width="1.3"><circle cx="8" cy="8" r="6.5"/><ellipse cx="8" cy="8" rx="3" ry="6.5"/><path d="M1.5 8h13"/></g></svg>
        <span>www.velourstudio.com</span>
      </li>
      <li class="contact__item">
        <svg class="contact__icon" viewBox="0 0 16 16" aria-hidden="true"><path d="M8 0.8a5 5 0 0 1 5 5c0 3.8-5 9.4-5 9.4S3 9.6 3 5.8a5 5 0 0 1 5-5zm0 3a2 2 0 1 0 0 4 2 2 0 0 0 0-4z"/></svg>
        <span>18 Linden Row, Ashford Vale<br>P.O Box 4410 Westmere</span>
      </li>
    </ul>

    <div class="social">
      <span class="social__mark"></span>
      <span>@velourstudio</span>
    </div>
  </section>

</main>
</body>
</html>
```